B2B Energy Broker Website

Our current website looks amateur, we need something far more professional looking and advanced. Current website is www.halvorn-utilitypartners.com

```html
<!DOCTYPE html>
<html lang="en">
<head>
<meta charset="utf-8">
<title>Halvorn Utility Partners – Transparent Energy Savings</title>
<link rel="stylesheet" href="https://fonts.googleapis.com/css2?family=Montserrat:wght@300;400;500;600;700&display=swap">
<style>
:root{
  --navy:#0a0c3a;
  --navy-deep:#080a30;
  --indigo:#1a1690;
  --footer:#15156a;
  --bar:#3320c8;
  --white:#ffffff;
  --text-soft:#d9dcf5;
  --cyan:#18c6f0;
  --blue:#1c8cf2;
  --violet:#7a4ce0;
  --magenta:#c31fe0;
  --orange:#f0602e;
  --accent:#27d4f5;
  --line:rgba(120,200,230,.55);
}
*{margin:0;padding:0;box-sizing:border-box}
html,body{width:1200px;height:3114px;overflow:hidden}
body{
  position:relative;
  font-family:"Montserrat",sans-serif;
  color:var(--white);
  background:linear-gradient(180deg,#141a5c 0,#0d1048 420px,var(--navy) 700px,var(--navy) 1600px,var(--indigo) 1900px,#12127a 2150px,var(--navy-deep) 2500px,var(--navy-deep) 2927px);
}
.abs{position:absolute}
.hero-art{left:0;top:0;width:1200px;height:480px;
  background:radial-gradient(ellipse 420px 260px at 160px 260px,rgba(70,110,220,.45),transparent 70%),
             radial-gradient(ellipse 220px 160px at 1120px 40px,rgba(120,140,255,.35),transparent 70%);}
.ring{border:1px solid var(--line);border-radius:50%}
.topbar{left:701px;top:0;width:255px;height:25px;background:var(--bar);font-size:9px;line-height:25px;text-align:center}
.brand{display:flex;align-items:center;gap:8px}
.brand-mark{width:36px;height:36px;border-radius:50%;background:var(--white)}
.brand-name{font-weight:500;font-size:15px;line-height:1.05;letter-spacing:2px;text-transform:uppercase}
.nav{top:53px;left:660px;display:flex;gap:0;font-size:10.5px}
.nav a{color:var(--white);text-decoration:none;position:absolute;white-space:nowrap}
.nav a.active{color:var(--accent);font-weight:700}
.hero-title{top:186px;width:1200px;text-align:center;font-weight:700;font-size:27px;letter-spacing:.5px}
.hero-sub{top:239px;width:1200px;text-align:center;font-size:13px}
.center{width:1200px;text-align:center}
.kicker{font-weight:700;font-size:12.5px}
.section-title{font-weight:400;font-size:26px;letter-spacing:.5px;text-transform:uppercase}
.intro{left:324px;width:552px;text-align:center;font-size:9.3px;line-height:22.4px;color:var(--text-soft)}
.btn{background:var(--white);color:#0a0c3a;font-weight:700;font-size:8.5px;border-radius:14px;text-align:center;text-transform:uppercase;letter-spacing:.3px}
.svc-title{font-weight:400;font-size:19.5px;text-transform:uppercase;letter-spacing:.3px}
.svc-text{font-size:9.3px;line-height:22.5px;color:var(--text-soft);width:310px}
.illus{border-radius:50%}
.strip{left:236px;top:1872px;width:727px;height:108px;background:#eceef3;display:flex;align-items:center;justify-content:space-around;padding:0 20px}
.supplier{font-weight:600;font-size:17px;color:#2a3a8a}
.feature{width:240px;text-align:center}
.feature h3{font-weight:400;font-size:18px;margin-top:0}
.feature p{font-size:9.3px;line-height:22.6px;color:var(--text-soft);margin-top:12px}
.feature-box{left:488px;top:2062px;width:224px;height:348px;border:1px solid rgba(110,120,230,.6)}
.faq-q{font-weight:700;font-size:14.5px;text-transform:uppercase;letter-spacing:.3px}
.faq-a{font-size:10.2px;line-height:22.6px;color:var(--text-soft);width:500px}
.footer{left:0;top:2927px;width:1200px;height:187px;background:linear-gradient(180deg,var(--footer),#101060)}
.f-item{font-size:10.5px;color:var(--text-soft)}
.social{width:28px;height:28px;border-radius:50%;background:#3a2ad8}
</style>
</head>
<body>

<div class="abs hero-art" role="img" aria-label="Dark blue backdrop with glowing solar panel grid and light particles"></div>
<div class="abs ring" style="left:355px;top:-123px;width:488px;height:488px"></div>
<div class="abs ring" style="left:850px;top:346px;width:174px;height:174px"></div>

<div class="abs topbar">Tel: 0333 410 7265 | info@halvorn-utilitypartners.com</div>

<header>
  <div class="abs brand" style="left:244px;top:23px">
    <span class="brand-mark"></span>
    <span class="brand-name">Halvorn<br>Utility</span>
  </div>
  <nav class="abs nav">
    <a class="active" style="left:0">Home</a>
    <a style="left:55px">About Us</a>
    <a style="left:126px">Services</a>
    <a style="left:190px">FAQs</a>
    <a style="left:240px">Contact Us</a>
  </nav>
</header>

<h1 class="abs hero-title">TRANSPARENT ENERGY SAVINGS</h1>
<p class="abs hero-sub">Unbiased for your Business</p>

<svg class="abs" style="left:587px;top:389px" width="25" height="38" viewBox="0 0 25 38">
  <rect x="1" y="1" width="23" height="36" rx="11" fill="none" stroke="#fff" stroke-width="1.5"/>
  <path d="M12.5 12v14M8 21.5l4.5 4.5 4.5-4.5" fill="none" stroke="#fff" stroke-width="1.5"/>
</svg>

<section>
  <p class="abs center kicker" style="top:497px">WELCOME TO</p>
  <h2 class="abs center section-title" style="top:531px;font-weight:300">Halvorn Utility Partners</h2>
  <svg class="abs" style="left:550px;top:579px" width="107" height="14" viewBox="0 0 107 14"><path d="M2 11L12.5 3 23 11 33.5 3 44 11 54.5 3 65 11 75.5 3 86 11 96.5 3 105 11" fill="none" stroke="var(--blue)" stroke-width="2.5"/></svg>
  <p class="abs intro" style="top:623px">Along with providing competitive business energy procurement, we run a complete service solution for your ongoing energy requirements. We can take total management of your bills, supplier relationship, renewals and more. If you are concerned about a more complex arrangement for your energy supply then we will endeavour to take over the time spent on it and allow you as much or as little involvement as you desire.</p>
  <div class="abs btn" style="left:552px;top:735px;width:97px;height:27px;line-height:27px">About Us</div>
</section>

<section>
  <h2 class="abs center section-title" style="top:834px">Our Services</h2>
  <div class="abs" style="left:599px;top:876px;width:1px;height:55px;background:var(--line)"></div>
  <div class="abs" style="left:596px;top:931px;width:7px;height:7px;border-radius:50%;background:#5a6ad8"></div>

  <svg class="abs" style="left:255px;top:902px" width="107" height="14" viewBox="0 0 107 14"><path d="M2 11L12.5 3 23 11 33.5 3 44 11 54.5 3 65 11 75.5 3 86 11 96.5 3 105 11" fill="none" stroke="var(--cyan)" stroke-width="2.5"/></svg>
  <h3 class="abs svc-title" style="left:257px;top:929px">Commercial Gas</h3>
  <p class="abs svc-text" style="left:258px;top:960px">We offer an impartial review of your business gas requirements to ensure you are getting the best prices, service and management as a total package.</p>
  <div class="abs illus" style="left:695px;top:870px;width:187px;height:157px;background:radial-gradient(circle,rgba(60,120,255,.55),rgba(40,60,200,.2) 55%,transparent 72%)" role="img" aria-label="Glowing neon leaf shaped drops with circuit lines"></div>

  <div class="abs illus" style="left:322px;top:1088px;width:135px;height:169px;background:radial-gradient(circle,rgba(70,110,255,.5),rgba(40,50,180,.2) 55%,transparent 72%)" role="img" aria-label="Glowing neon light bulb with a sprouting plant"></div>
  <svg class="abs" style="left:652px;top:1108px" width="107" height="14" viewBox="0 0 107 14"><path d="M2 11L12.5 3 23 11 33.5 3 44 11 54.5 3 65 11 75.5 3 86 11 96.5 3 105 11" fill="none" stroke="var(--violet)" stroke-width="2.5"/></svg>
  <h3 class="abs svc-title" style="left:650px;top:1137px">Commercial Electricity</h3>
  <p class="abs svc-text" style="left:650px;top:1170px;width:310px">We offer an impartial review of your business electricity requirements to ensure you are getting the best prices, service and management as a total package.</p>

  <svg class="abs" style="left:255px;top:1309px" width="107" height="14" viewBox="0 0 107 14"><path d="M2 11L12.5 3 23 11 33.5 3 44 11 54.5 3 65 11 75.5 3 86 11 96.5 3 105 11" fill="none" stroke="var(--magenta)" stroke-width="2.5"/></svg>
  <h3 class="abs svc-title" style="left:257px;top:1341px">Utility Services</h3>
  <p class="abs svc-text" style="left:258px;top:1373px;width:290px">We can provide a wide range of business utility management services to ensure your time and money is better spent.</p>
  <div class="abs illus" style="left:728px;top:1293px;width:120px;height:169px;background:radial-gradient(circle,rgba(60,130,255,.5),rgba(40,60,200,.2) 55%,transparent 72%)" role="img" aria-label="Glowing neon battery with a sprouting leaf"></div>

  <div class="abs illus" style="left:308px;top:1511px;width:175px;height:193px;background:radial-gradient(circle,rgba(90,90,255,.55),rgba(70,40,200,.2) 55%,transparent 72%)" role="img" aria-label="Glowing neon water drop with ripples"></div>
  <svg class="abs" style="left:652px;top:1543px" width="107" height="14" viewBox="0 0 107 14"><path d="M2 11L12.5 3 23 11 33.5 3 44 11 54.5 3 65 11 75.5 3 86 11 96.5 3 105 11" fill="none" stroke="var(--orange)" stroke-width="2.5"/></svg>
  <h3 class="abs svc-title" style="left:650px;top:1570px">Commercial Water</h3>
  <p class="abs svc-text" style="left:650px;top:1600px;width:290px">The commercial water market has now been de-regulated. Speak to our team to find out how we can save you money on your water and waste bills.</p>
</section>

<section aria-label="Our suppliers">
  <svg class="abs" style="left:203px;top:1914px" width="14" height="18" viewBox="0 0 14 18"><path d="M11 2L4 9l7 7" fill="none" stroke="#fff" stroke-width="3"/></svg>
  <div class="abs strip">
    <span class="supplier">Arvela</span>
    <span class="supplier">Twinmere</span>
    <span class="supplier">Ostra</span>
    <span class="supplier">Glenmark</span>
    <span class="supplier">Solvane</span>
    <span class="supplier">Kestrel Gas</span>
  </div>
  <svg class="abs" style="left:986px;top:1914px" width="14" height="18" viewBox="0 0 14 18"><path d="M3 2l7 7-7 7" fill="none" stroke="#fff" stroke-width="3"/></svg>
</section>

<section>
  <div class="abs feature-box"></div>

  <div class="abs feature" style="left:216px;top:2106px">
    <svg width="56" height="56" viewBox="0 0 56 56"><circle cx="28" cy="28" r="25" fill="none" stroke="var(--blue)" stroke-width="3"/><path d="M28 28V3M28 28L50 40M28 28L6 40" stroke="var(--blue)" stroke-width="3"/><path d="M31 6a22 22 0 0 1 19 30L31 26z" fill="var(--cyan)" opacity=".7"/></svg>
    <h3 style="margin-top:20px">Market Trend Analysis</h3>
    <p>Our energy analysts monitor a live energy market curve to ensure you buy at the right time and save as much as possible.</p>
    <svg style="margin-top:14px" width="30" height="30" viewBox="0 0 30 30"><rect x="6" y="6" width="18" height="18" transform="rotate(45 15 15)" fill="none" stroke="#6a5ae8" stroke-width="1.5"/><path d="M13 10.5l4.5 4.5-4.5 4.5" fill="none" stroke="#fff" stroke-width="1.6"/></svg>
  </div>

  <div class="abs feature" style="left:479px;top:2102px">
    <svg width="62" height="60" viewBox="0 0 62 60"><rect x="23" y="2" width="16" height="13" fill="none" stroke="var(--blue)" stroke-width="3"/><path d="M31 15v12M11 27h40M11 27v8M31 27v18M51 27v8" stroke="var(--blue)" stroke-width="3" fill="none"/><rect x="3" y="35" width="16" height="13" fill="none" stroke="var(--blue)" stroke-width="3"/><rect x="43" y="35" width="16" height="13" fill="none" stroke="var(--blue)" stroke-width="3"/><rect x="23" y="45" width="16" height="13" fill="none" stroke="var(--blue)" stroke-width="3"/></svg>
    <h3 style="margin-top:20px">Direct Relationships</h3>
    <p>We hold direct relationships with over 18 major suppliers, we use these relationships to ensure you get the most from your supplier.</p>
    <svg style="margin-top:14px" width="30" height="30" viewBox="0 0 30 30"><rect x="6" y="6" width="18" height="18" transform="rotate(45 15 15)" fill="none" stroke="#6a5ae8" stroke-width="1.5"/><path d="M13 10.5l4.5 4.5-4.5 4.5" fill="none" stroke="#fff" stroke-width="1.6"/></svg>
  </div>

  <div class="abs feature" style="left:742px;top:2098px">
    <svg width="66" height="64" viewBox="0 0 66 64"><circle cx="33" cy="20" r="10" fill="none" stroke="var(--blue)" stroke-width="3"/><circle cx="33" cy="20" r="16" fill="none" stroke="var(--blue)" stroke-width="3" stroke-dasharray="6 4"/><path d="M4 30v16l14 14h10M62 30v16L48 60H38" fill="none" stroke="var(--blue)" stroke-width="3"/></svg>
    <h3 style="margin-top:18px">Industry Experience</h3>
    <p>Our two founders hold over 30 years industry experience between them and our staff are what we believe to be the best in the industry.</p>
    <svg style="margin-top:14px" width="30" height="30" viewBox="0 0 30 30"><rect x="6" y="6" width="18" height="18" transform="rotate(45 15 15)" fill="none" stroke="#6a5ae8" stroke-width="1.5"/><path d="M13 10.5l4.5 4.5-4.5 4.5" fill="none" stroke="#fff" stroke-width="1.6"/></svg>
  </div>
</section>

<section>
  <h2 class="abs section-title" style="left:251px;top:2564px">FAQ</h2>
  <svg class="abs" style="left:248px;top:2606px" width="107" height="14" viewBox="0 0 107 14"><path d="M2 11L12.5 3 23 11 33.5 3 44 11 54.5 3 65 11 75.5 3 86 11 96.5 3 105 11" fill="none" stroke="var(--blue)" stroke-width="2.5"/></svg>
  <h3 class="abs faq-q" style="left:247px;top:2660px">Why should my business use Halvorn Utility Partners?</h3>
  <p class="abs faq-a" style="left:248px;top:2700px">We provide an unbiased &amp; transparent cost effective solution to all your business energy needs. In essence, with over 3 decades experience in the UK energy Industry. We have both the expertise &amp; know how to manage your business energy requirements. Our philosophy is simple solutions with transparency.</p>
  <div class="abs btn" style="left:244px;top:2824px;width:97px;height:26px;line-height:26px">View All</div>
  <div class="abs illus" style="left:782px;top:2544px;width:207px;height:260px;background:radial-gradient(ellipse at 50% 45%,rgba(40,170,240,.55),rgba(30,80,200,.25) 55%,transparent 72%)" role="img" aria-label="Glowing blue question mark made of light particles"></div>
</section>

<footer class="abs footer">
  <div class="abs brand" style="left:249px;top:68px">
    <span class="brand-mark" style="width:42px;height:42px"></span>
    <span class="brand-name" style="font-size:17px">Halvorn<br>Utility</span>
  </div>

  <svg class="abs" style="left:469px;top:52px" width="10" height="13" viewBox="0 0 10 13"><path d="M5 12S1 7.5 1 5a4 4 0 0 1 8 0c0 2.5-4 7-4 7z" fill="#fff"/><circle cx="5" cy="5" r="1.5" fill="#15156a"/></svg>
  <p class="abs f-item" style="left:497px;top:52px">Unit 4, 12 Farrow Lane, Leicester, LE4 2PQ</p>

  <svg class="abs" style="left:469px;top:92px" width="11" height="11" viewBox="0 0 11 11"><path d="M2 1l2 .3.8 2.4-1.2 1a6 6 0 0 0 2.7 2.7l1-1.2 2.4.8L10 9c0 .6-.5 1-1 1A8.5 8.5 0 0 1 1 2c0-.5.4-1 1-1z" fill="#fff"/></svg>
  <p class="abs f-item" style="left:497px;top:91px">0333 410 7265</p>
  <svg class="abs" style="left:594px;top:92px" width="11" height="11" viewBox="0 0 11 11"><rect x="1" y="3" width="9" height="7" fill="#fff"/><rect x="3" y="0.5" width="5" height="3" fill="none" stroke="#fff"/></svg>
  <p class="abs f-item" style="left:621px;top:91px">0333 410 7265</p>

  <svg class="abs" style="left:469px;top:127px" width="12" height="9" viewBox="0 0 12 9"><rect width="12" height="9" fill="#fff"/><path d="M0 0l6 5 6-5" fill="none" stroke="#15156a"/></svg>
  <p class="abs f-item" style="left:497px;top:125px">info@halvorn-utilitypartners.com</p>

  <p class="abs f-item" style="left:810px;top:53px;letter-spacing:1.5px;color:#fff">Stay in touch</p>
  <span class="abs social" style="left:804px;top:81px" aria-label="Social link"></span>
  <span class="abs social" style="left:843px;top:81px" aria-label="Social link"></span>
  <span class="abs social" style="left:880px;top:81px" aria-label="Social link"></span>
  <span class="abs social" style="left:917px;top:81px" aria-label="Social link"></span>
</footer>

</body>
</html>
```